Open House evite for our 7th Anniversary needs Invitation Design

Need an invitation design for an upcoming event. Our event is an Open House to celebrate our 7th anniversary with clients & business colleagues. We need a professional but fun invitation. We are a women owned law firm. We will use this design for a Save the Date, an evite, a hard invitation, an eReminder and a wine label.
Focus of design should be on the "7"!!! (this is new)
Every year the focus will be on the year.
We have 3 women partners who run the firm. If there is a way to incorporate that into the drawing-great! Attached is a sketch that focuses on the 7 and has three stick figure women. It has our logo "&" in the background and says "Seven Lucky Years & Still Going...." OPEN HOUSE....This is a thought, please play around with it. It does not have to have the women, but is one thought. We have a submittal on an elegant 7 that we liked, but did not hear back from the designer, so that is an option also. An elegant 7 in black, gray background, with blue or green as accent colors is something else we would like to see.

Please view our website: www.bhmcounsel.example for our colors. You do not need to use these, but it gives you an idea of the feel of our marketing.
Incorporate:
our logo, per attached

OPEN HOUSE:
June 4, 2015
3:00-7:00pm
Brisk, Hollin & Marrow, LLC
5218 Tamarind, Suite 400
Fern Hollow, IL 60099
RSVP to rsvp@bhmcounsel.example

We will only be sending out about 20 actual hard copy invites. We will be sending the evites through Steady Mailer and this is the heart of the project. We will send a Save the Date, then 2-3 weeks later an evite, then 2-4 weeks later a Reminder, and then the week before one more reminder.
The wine labels are used all year long and are the past years are all displayed in frames in our office. They are an important aspect of our marketing efforts.

Target Market(s)

Adults - clients & business colleagues

Industry/Entity Type

Business

Colors
000000
acd036
81c7e5

Requirements
Must have
• Focus the design on the "7". There is a sketched attached. This is not exactly what we want, but a thought. See attached.
• Incorporate our logo, per attached
• OPEN HOUSE:
• June 4, 2015
• 3:00-7:00pm
• Brisk, Hollin & Marrow, LLC
• 5218 Tamarind, Suite 400
• Fern Hollow, IL 60099
• RSVP to rsvp@bhmcounsel.example
Nice to have
• If you can incorporate 3 women lawyer figures into the design - great! Stick figures are ok.

```html
<!DOCTYPE html>
<html lang="en">
<head>
<meta charset="utf-8">
<title>Brisk, Hollin &amp; Marrow — 7th Anniversary Open House</title>
<link rel="stylesheet" href="https://fonts.googleapis.com/css2?family=Josefin+Sans:wght@300;400&family=Sacramento&display=swap">
<style>
  :root {
    --backdrop: #7d8aa8;
    --slate: #3d4542;
    --paper: #f7f7f5;
    --ink: #2f3532;
    --lime: #a6c436;
    --sky: #7d9fd3;
    --mist: #8a8f8c;
    --white: #ffffff;
  }
  * { margin: 0; padding: 0; box-sizing: border-box; }
  html, body { width: 1200px; height: 1000px; overflow: hidden; }
  body {
    background: var(--backdrop);
    font-family: "Josefin Sans", "Helvetica Neue", sans-serif;
    font-weight: 300;
    position: relative;
  }
  .card {
    position: absolute;
    top: 190px;
    width: 440px;
    height: 620px;
    box-shadow: 0 10px 28px rgba(30, 40, 70, 0.25);
    overflow: hidden;
  }
  .card > * { position: absolute; }
  .frame { inset: 0; width: 440px; height: 620px; }
  .script { font-family: "Sacramento", cursive; font-weight: 400; }

  /* Save the date */
  .save-date { left: 120px; background: var(--slate); color: var(--white); }
  .save-date .headline { left: 70px; font-size: 104px; line-height: 1; letter-spacing: 4px; }
  .save-date .word-save { top: 60px; }
  .save-date .word-the { top: 140px; left: 150px; font-size: 86px; color: var(--sky); line-height: 1; }
  .save-date .word-date { top: 200px; }
  .save-date .numeric-date { top: 330px; left: 110px; font-size: 38px; color: var(--sky); letter-spacing: 4px; }
  .save-date .firm-mark { top: 470px; left: 100px; display: flex; align-items: center; gap: 10px; font-size: 24px; color: var(--white); font-weight: 400; }
  .save-date .firm-mark .dot { width: 14px; height: 14px; border-radius: 50%; background: var(--white); }
  .save-date .tagline { top: 506px; left: 124px; font-size: 22px; color: var(--lime); font-weight: 400; }

  /* Invitation */
  .invitation { left: 640px; background: var(--paper); color: var(--ink); }
  .invitation .big { left: 40px; line-height: 1; letter-spacing: 2px; }
  .invitation .word-seventh { top: 36px; font-size: 128px; }
  .invitation .word-anniversary { top: 148px; left: 60px; font-size: 52px; color: var(--sky); line-height: 1; }
  .invitation .word-open { top: 196px; font-size: 100px; }
  .invitation .word-house { top: 270px; left: 120px; font-size: 96px; color: var(--lime); line-height: 1; }
  .invitation .event-time { top: 380px; left: 270px; font-size: 18px; color: var(--lime); font-weight: 400; letter-spacing: 1px; }
  .invitation .event-date { top: 438px; left: 42px; color: var(--sky); line-height: 0.95; font-weight: 400; }
  .invitation .event-date .month { font-size: 38px; display: block; }
  .invitation .event-date .year { font-size: 52px; display: block; }
  .invitation .venue { top: 440px; left: 256px; width: 180px; }
  .invitation .venue .firm { font-size: 17px; color: var(--sky); line-height: 1.15; letter-spacing: 1px; font-weight: 400; }
  .invitation .venue .address { margin-top: 6px; font-size: 11px; line-height: 1.35; font-weight: 400; }
  .invitation .venue .rsvp { margin-top: 10px; font-size: 10.5px; color: var(--lime); font-weight: 400; }
  .invitation .firm-mark { top: 560px; left: 44px; display: flex; align-items: center; gap: 8px; font-size: 18px; color: var(--mist); font-weight: 400; }
  .invitation .firm-mark .dot { width: 11px; height: 11px; border-radius: 50%; background: var(--mist); }
</style>
</head>
<body>

<section class="card save-date" aria-label="Save the date card">
  <svg class="frame" viewBox="0 0 440 620" aria-hidden="true">
    <path d="M40 0 V390 H330 L410 320 V0" fill="none" stroke="var(--lime)" stroke-width="3"/>
    <line x1="60" y1="316" x2="400" y2="300" stroke="var(--lime)" stroke-width="3"/>
  </svg>
  <p class="headline word-save">SAVE</p>
  <p class="script word-the">The</p>
  <p class="headline word-date">DATE</p>
  <p class="numeric-date">06 • 04 • 15</p>
  <p class="firm-mark"><span>Brisk Hollin Marrow</span><span class="dot"></span></p>
  <p class="tagline">7th Anniversary</p>
</section>

<section class="card invitation" aria-label="Open house invitation card">
  <svg class="frame" viewBox="0 0 440 620" aria-hidden="true">
    <path d="M440 330 L420 372 H268 L256 390 L268 408 H420 L420 372" fill="none" stroke="var(--lime)" stroke-width="2.5"/>
    <path d="M0 430 H210 L238 470 L210 540 H30 V430" fill="none" stroke="var(--sky)" stroke-width="2.5"/>
  </svg>
  <p class="big word-seventh">7TH</p>
  <p class="script word-anniversary">Anniversary</p>
  <p class="big word-open">OPEN</p>
  <p class="script word-house">House</p>
  <p class="event-time">3:00 – 7:00 PM</p>
  <p class="event-date"><span class="month">JUNE 4</span><span class="year">2015</span></p>
  <div class="venue">
    <p class="firm">BRISK, HOLLIN &amp;<br>MARROW, LLC</p>
    <p class="address">5218 Tamarind, Suite 400<br>Fern Hollow, IL 60099</p>
    <p class="rsvp">RSVP to rsvp@bhmcounsel.example</p>
  </div>
  <p class="firm-mark"><span>Brisk Hollin Marrow</span><span class="dot"></span></p>
</section>

</body>
</html>
```